Business card design needed

I need a business card for my private practice. I would like to see the designs that use bright blue and white. I would like to see similar designs as to the card below:
http://blog.printvarno.com/2009/designing-a-business-card-with-pv-ks517-template.html
I would like to see the back of the card have room for appointment times. Thank you.

Industry/Entity Type
Business
Contact Information for Business Card
Brightwater Counselling & Wellness Services
Helen Dorsey B.Psychology
Registered Psychologist
Building C, Level 3, 14 Marrow Crescent, Canberra, ACT 2601
T: (02) 6287 5912
F: (02) 6287 5930
info@brightwatercounselling.com.au
www.brightwatercounselling.com.au

```html
<!DOCTYPE html>
<html lang="en">
<head>
<meta charset="utf-8">
<title>Brightwater Counselling &amp; Wellness Services – Business Card</title>
<link rel="stylesheet" href="https://fonts.googleapis.com/css2?family=Open+Sans:wght@600;700;800&display=swap">
<style>
  :root {
    --bg: #262626;
    --blue-deep: #0a4fc4;
    --blue: #1a73f0;
    --blue-bright: #3d9bff;
    --blue-text: #0b3f9e;
    --accent-text: #1a73f0;
    --white: #ffffff;
    --white-soft: #dcebff;
  }
  * { box-sizing: border-box; margin: 0; padding: 0; }
  html, body { width: 1200px; height: 1200px; overflow: hidden; }
  body {
    background: var(--bg);
    font-family: "Open Sans", Verdana, sans-serif;
    position: relative;
  }
  .card {
    position: absolute;
    left: 160px;
    width: 880px;
    height: 500px;
    border-radius: 26px;
    overflow: hidden;
  }

  /* Front */
  .card-front {
    top: 60px;
    background: linear-gradient(180deg, var(--blue-deep) 0%, var(--blue) 60%, var(--blue-bright) 100%);
  }
  .card-front .band-accent {
    position: absolute; left: 0; right: 0; bottom: 0; height: 34px;
    background: var(--white);
  }
  .brand {
    position: absolute; left: 0; right: 0; top: 160px;
    text-align: center;
  }
  .brand-name {
    display: inline-flex; align-items: center; gap: 18px;
    color: var(--white); font-weight: 800; font-size: 82px; line-height: 1;
    letter-spacing: 1px;
  }
  .brand-mark {
    width: 40px; height: 40px; border-radius: 50%; background: var(--white);
  }
  .brand-tagline {
    margin-top: 22px;
    color: var(--white-soft); font-weight: 600; font-size: 30px; letter-spacing: 1px;
  }

  /* Back */
  .card-back {
    top: 640px;
    background: var(--white);
  }
  .card-back .band-top {
    position: absolute; left: 0; right: 0; top: 0; height: 32px;
    background: var(--blue-bright);
  }
  .card-back .band-bottom {
    position: absolute; left: 0; right: 0; bottom: 0; height: 34px;
    background: var(--blue-deep);
  }
  .person {
    position: absolute; left: 56px; top: 150px;
    font-weight: 700;
  }
  .person-name { color: var(--blue-text); font-size: 40px; font-weight: 800; letter-spacing: 1px; }
  .person-degree { color: var(--accent-text); font-size: 26px; margin-top: 2px; }
  .person-title { color: var(--blue-text); font-size: 26px; }
  .divider {
    position: absolute; left: 430px; top: 60px; width: 3px; height: 200px;
    background: linear-gradient(180deg, transparent, var(--blue) 15%, var(--blue) 85%, transparent);
  }
  .contact {
    position: absolute; left: 460px; top: 62px;
    font-size: 21px; font-weight: 700; line-height: 1.28;
  }
  .contact-address { color: var(--blue-text); margin-bottom: 12px; }
  .contact-line { color: var(--blue-text); }
  .contact-line .label { color: var(--accent-text); }
  .contact-web { color: var(--accent-text); }
  .appointment {
    position: absolute; left: 56px; right: 56px; top: 320px;
    font-weight: 700;
  }
  .appointment-title { color: var(--accent-text); font-size: 26px; margin-bottom: 24px; }
  .appointment-fields { display: flex; align-items: flex-end; gap: 10px; color: var(--blue-text); font-size: 24px; }
  .field-line { flex: 1; border-bottom: 3px dotted var(--blue-text); margin-bottom: 7px; }
</style>
</head>
<body>
  <section class="card card-front" aria-label="Card front">
    <div class="brand">
      <div class="brand-name"><span class="brand-mark"></span>Brightwater</div>
      <div class="brand-tagline">Counselling &amp; Wellness Services</div>
    </div>
    <div class="band-accent"></div>
  </section>

  <section class="card card-back" aria-label="Card back">
    <div class="band-top"></div>
    <div class="person">
      <div class="person-name">Helen Dorsey</div>
      <div class="person-degree">B.Psychology</div>
      <div class="person-title">Registered Psychologist</div>
    </div>
    <div class="divider"></div>
    <div class="contact">
      <div class="contact-address">Building C, Level 3,<br>14 Marrow Crescent,<br>Canberra, ACT 2601</div>
      <div class="contact-line"><span class="label">T:</span> (02) 6287 5912</div>
      <div class="contact-line"><span class="label">F:</span> (02) 6287 5930</div>
      <div class="contact-web">info@brightwatercounselling.com.au</div>
      <div class="contact-web">www.brightwatercounselling.com.au</div>
    </div>
    <div class="appointment">
      <div class="appointment-title">Next appointment</div>
      <div class="appointment-fields">
        <span>Day</span><span class="field-line"></span>
        <span>Date</span><span class="field-line"></span>
        <span>Time</span><span class="field-line"></span>
      </div>
    </div>
    <div class="band-bottom"></div>
  </section>
</body>
</html>
```